Brindle's Custom Signs and Woodworking Business Card

I run a small business that does custom woodworking and sign making. I have a logo already that I am very fond of, and would like to continue with the theme of the logo. I'd like a business card that adds onto that theme/design and stands out among typical business cards. As you'll be able to see from the logo, we're a patriotic brand and that is paramount to us.
Contact Information for Business Card
beneath the Brindle's logo, I'd like it to say
"Custom Signs & Woodworking"
Also, I'd like the following information template present on the card, preferably with the logos of instagram and facebook present besides the title.
(Name)                                 (Instragram)
(Email)                                  (Facebook)
(Phone)                                 (Website)
I would like for the name, email, and phone number to be editable so that I can have my employees utilize this card design as well. but for my card, my information is as follows
Dan "Brindle" Korvell, CEO                                           @BrindlesCustoms
Dan@BrindlesCustoms.example                                          Brindle's Customs
(555) 274-6103                                                         BrindlesCustoms.example
As for the back side, either a full american flag, or something that catches the eye, designer's preference I suppose.
Font styles to use
Other font styles liked:
- Funkydori, an adobe typekit font. it is the same as used for the logo. I'm not sure how the whole card will look with that, so if it doesn't look right please use something that complements the script style of the logo

```html
<!DOCTYPE html>
<html lang="en">
<head>
<meta charset="utf-8">
<title>Brindle's Custom Signs and Woodworking – Business Card</title>
<link rel="stylesheet" href="https://fonts.googleapis.com/css2?family=Roboto:wght@400;500;700;900&display=swap">
<style>
  :root {
    --backdrop: #3b3b3d;
    --paper: #f3f3f3;
    --navy: #0f2466;
    --red: #b01c2e;
    --white: #ffffff;
    --wash-red: #efd3d7;
    --wash-blue: #dcdfea;
  }
  * { margin: 0; padding: 0; box-sizing: border-box; }
  html, body {
    width: 1200px; height: 960px; overflow: hidden;
    background: var(--backdrop);
    font-family: "Roboto", Arial, sans-serif;
  }
  .card {
    position: absolute;
    width: 598px; height: 342px;
    background: var(--paper);
    overflow: hidden;
    box-shadow: 0 3px 8px rgba(0,0,0,.45);
  }
  .card--front { left: 322px; top: 110px; }
  .card--back { left: 320px; top: 493px; }
  .card__wave { position: absolute; inset: 0; }

  .brand-name {
    position: absolute;
    color: var(--navy);
    font-weight: 900;
    letter-spacing: -1px;
    line-height: 1;
  }
  .card--front .brand-name { left: 40px; top: 78px; font-size: 58px; }

  .contact {
    position: absolute;
    right: 26px; top: 174px;
    color: var(--white);
    text-align: right;
  }
  .contact__name { font-size: 21px; font-weight: 700; line-height: 26px; padding-right: 2px; }
  .contact__title { font-size: 15px; font-weight: 400; line-height: 20px; margin-bottom: 8px; padding-right: 2px; }
  .contact__list { list-style: none; }
  .contact__item {
    display: flex; justify-content: flex-end; align-items: center;
    gap: 8px; font-size: 15px; line-height: 19.5px;
  }
  .contact__icon { width: 13px; height: 13px; flex: none; }

  .back-wash {
    position: absolute; inset: 0;
    background: linear-gradient(150deg, var(--wash-blue) 0%, var(--wash-red) 40%, var(--paper) 85%);
  }
  .back-logo {
    position: absolute; left: 335px; top: 168px; width: 240px;
  }
  .card--back .brand-name { position: static; font-size: 60px; }
  .tagline {
    margin-top: 22px;
    color: var(--navy);
    font-size: 17px; font-weight: 700;
  }
</style>
</head>
<body>

<section class="card card--front" aria-label="Business card front">
  <svg class="card__wave" viewBox="0 0 598 342" width="598" height="342" aria-hidden="true">
    <path d="M0,212 C30,290 120,288 250,218 S470,86 598,96 L598,342 L0,342 Z" fill="var(--white)"/>
    <path d="M0,215 C30,290 120,285 250,220 S470,90 598,100 L598,342 L0,342 Z" fill="var(--navy)"/>
    <path d="M0,232 C40,298 130,294 255,238 S480,108 598,112 L598,342 L0,342 Z" fill="var(--white)"/>
    <path d="M0,235 C40,300 130,297 255,241 S480,111 598,115 L598,342 L0,342 Z" fill="var(--red)"/>
  </svg>

  <div class="brand-name">Brindle's</div>

  <div class="contact">
    <div class="contact__name">Dan "Brindle" Korvell</div>
    <div class="contact__title">CEO</div>
    <ul class="contact__list">
      <li class="contact__item">(555) 274-6103
        <svg class="contact__icon" viewBox="0 0 16 16" aria-hidden="true"><path d="M3 1l3 3-2 2c1 2 3 4 5 5l2-2 3 3-2 3C7 15 1 9 0 3z" fill="var(--white)"/></svg></li>
      <li class="contact__item">/Brindle's Customs
        <svg class="contact__icon" viewBox="0 0 16 16" aria-hidden="true"><rect width="16" height="16" rx="2" fill="var(--white)"/></svg></li>
      <li class="contact__item">@BrindlesCustoms
        <svg class="contact__icon" viewBox="0 0 16 16" aria-hidden="true"><circle cx="8" cy="8" r="8" fill="var(--white)"/></svg></li>
      <li class="contact__item">Dan@BrindlesCustoms.example
        <svg class="contact__icon" viewBox="0 0 16 16" aria-hidden="true"><rect y="3" width="16" height="11" fill="var(--white)"/><path d="M0 3l8 6 8-6" fill="none" stroke="var(--red)" stroke-width="1.5"/></svg></li>
      <li class="contact__item">www.BrindlesCustoms.example
        <svg class="contact__icon" viewBox="0 0 16 16" aria-hidden="true"><circle cx="8" cy="8" r="7.5" fill="var(--white)"/><path d="M1 8h14M8 1c-3 4-3 10 0 14M8 1c3 4 3 10 0 14" fill="none" stroke="var(--red)" stroke-width="1.2"/></svg></li>
    </ul>
  </div>
</section>

<section class="card card--back" aria-label="Business card back">
  <div class="back-wash" role="img" aria-label="Faint waving American flag illustration in the background"></div>
  <div class="back-logo">
    <div class="brand-name">Brindle's</div>
    <div class="tagline">Custom Signs &amp; Woodworking</div>
  </div>
</section>

</body>
</html>
```